Fernvale Business Card Design

We are looking for a fresh business card design for our new logo. We would like a business card that is unique but friendly. We are in the window coverings business offering blinds, shutters and shades for homes.

Target Market(s)

Targeting the end-consumer

Industry/Entity Type

Business

Requirements
Must have
• Must have a dedicates space for a photo of our sales person. Must contain our new logo (attached).

```html
<!DOCTYPE html>
<html lang="en">
<head>
<meta charset="utf-8">
<title>Fernvale Business Card</title>
<link href="https://fonts.googleapis.com/css2?family=Oswald:wght@300;400;500&display=swap" rel="stylesheet">
<style>
  :root {
    --bg: #ece9e4;
    --card: #ffffff;
    --green: #8cc43f;
    --grey: #666669;
    --white: #ffffff;
    --photo-top: #d9d2cc;
    --photo-bottom: #b0485a;
  }
  html, body {
    margin: 0;
    width: 1200px;
    height: 1200px;
    overflow: hidden;
    background: var(--bg);
    font-family: "Oswald", "Arial Narrow", sans-serif;
  }
  .canvas { position: relative; width: 1200px; height: 1200px; }
  .card {
    position: absolute;
    left: 146px;
    width: 907px;
    height: 518px;
    background: var(--card);
    overflow: hidden;
    box-shadow: 0 6px 18px rgba(0,0,0,0.18);
  }
  .card--front { top: 52px; border-radius: 170px 8px 170px 8px; }
  .card--back { top: 618px; border-radius: 8px 170px 8px 170px; }

  .contact-panel {
    position: absolute;
    left: 86px; top: 48px;
    width: 474px; height: 372px;
    background: var(--green);
    border-radius: 120px 0 0 0;
    color: var(--white);
  }
  .contact-panel::after {
    content: "";
    position: absolute;
    right: -8px; top: 0;
    width: 90px; height: 100%;
    background: var(--card);
    border-radius: 70px 0 0 0;
  }
  .person-name {
    position: absolute; left: 46px; top: 80px;
    margin: 0; font-size: 40px; font-weight: 500; letter-spacing: 0.5px;
    line-height: 1;
  }
  .person-role {
    position: absolute; left: 46px; top: 128px;
    margin: 0; font-size: 22px; font-weight: 300;
  }
  .address {
    position: absolute; left: 50px; top: 182px;
    margin: 0; font-size: 21px; font-weight: 300; line-height: 29px;
    font-style: normal;
  }
  .contact-list {
    position: absolute; left: 48px; top: 262px;
    margin: 0; padding: 0; list-style: none;
    font-size: 21px; font-weight: 300;
  }
  .contact-list li { display: flex; align-items: center; height: 37px; }
  .contact-list svg { width: 22px; height: 22px; margin-right: 12px; fill: var(--white); }

  .brand-frame {
    position: absolute;
    left: 420px; top: 56px;
    width: 402px; height: 412px;
    display: flex; align-items: center; justify-content: center; gap: 18px;
  }
  .brand-mark { width: 40px; height: 40px; background: var(--green); }
  .brand-name {
    font-size: 72px; font-weight: 400; color: var(--grey); line-height: 1;
  }

  .back-brand {
    position: absolute; left: 50px; top: 102px;
    display: flex; align-items: center; gap: 26px;
  }
  .back-brand .brand-mark { width: 98px; height: 98px; background: none; border: 5px solid var(--grey); box-sizing: border-box; border-radius: 4px 4px 18px 4px; }
  .back-brand .brand-name { font-size: 68px; }

  .staff-photo {
    position: absolute;
    left: 478px; top: 50px;
    width: 429px; height: 468px;
    background: linear-gradient(180deg, var(--photo-top) 0%, #c99a92 35%, var(--photo-bottom) 100%);
  }
</style>
</head>
<body>
<main class="canvas">
  <section class="card card--front">
    <div class="contact-panel">
      <h1 class="person-name">DANIEL MOORE</h1>
      <p class="person-role">Director</p>
      <address class="address">420 Maple Grove Lane<br>Westbrook, CA 90210</address>
      <ul class="contact-list">
        <li>
          <svg viewBox="0 0 24 24" aria-hidden="true"><path d="M6.6 10.8a15.1 15.1 0 0 0 6.6 6.6l2.2-2.2c.3-.3.7-.4 1-.2 1.1.4 2.3.6 3.6.6.6 0 1 .4 1 1V20c0 .6-.4 1-1 1A17 17 0 0 1 3 4c0-.6.4-1 1-1h3.5c.6 0 1 .4 1 1 0 1.3.2 2.5.6 3.6.1.3 0 .7-.2 1z"/></svg>
          555.214.7830
        </li>
        <li>
          <svg viewBox="0 0 24 24" aria-hidden="true"><path d="M2 5h20v14H2z M3.5 6.5 12 13l8.5-6.5v-.1H3.5z" fill-rule="evenodd"/><path d="M2 5l10 8 10-8v1.6l-10 8-10-8z" fill="#8cc43f"/></svg>
          info@fernvale.com
        </li>
        <li>
          <svg viewBox="0 0 24 24" aria-hidden="true"><circle cx="12" cy="12" r="10"/><path d="M7 7c2 0 3 1 3 3s-2 2-2 4 1 3 1 5M15 4c-1 2 0 3 2 4s3 2 4 2" stroke="#8cc43f" stroke-width="1.6" fill="none"/></svg>
          www.fernvale.com
        </li>
      </ul>
    </div>
    <div class="brand-frame">
      <span class="brand-name">Fernvale</span>
    </div>
  </section>

  <section class="card card--back">
    <div class="back-brand">
      <span class="brand-mark"></span>
      <span class="brand-name">Fernvale</span>
    </div>
    <div class="staff-photo" role="img" aria-label="Photo of the sales representative, arms crossed, wearing a red plaid shirt"></div>
  </section>
</main>
</body>
</html>
```